WordPress Website Design - Tolvey Auction

Need a WordPress design for an auction company wanting a responsive, simple and easy to use site.
Sites the client mentions liking - www.brindlegavel.example, http://www.quellor.example and http://www.pardwick.example/. The logo is attached. Site color can be changed to suit your design. Also consider the attached graphic for email lists.

Industry/Entity Type

It Company

Number of Pages Required

1 page

Font styles to use
Serif
Sans Serif

Requirements
Must have
• Will be graphic intensive with full width slideshow. tagline to be used – “Let Our Experience Work for You! The background of the site can be the background of the attached image. The feel of the site can be the attached email template.
• Navigation: 1)Home 2) Tolvey Services 3) Featured Projects 4) Results 5) Buying/Selling 6) About Tolvey 7) Contact us
• Colors will be those on current site and those in the email template.
• Calls to action on the homepage:1) Marketing Consultation, 2) Marketing Plan Implementation, 3) Coordination of Related Marketing Services, 4)Featured Projects, 5) Negotiated Sales
• widgets can include upcoming auctions, email signup, news & events
• Choice of the company logo to use- light or dark.
• Footer will have contact info, a testimonial widget,and associated logos (attached)
• contact info:
• Tolvey Companies, Inc
• P.O. Box 4382
• Rochester, MN 55961
• tolvey@tolveycompanies.example
• (507) 555-0187 • Fax (507) 555-0143
Nice to have
• Use of drop down menus - under "Results"
• 1) Auction Results
• 2) Sales results

```html
<!DOCTYPE html>
<html lang="en">
<head>
<meta charset="utf-8">
<title>Tolvey Companies – Let Our Experience Work for You!</title>
<link rel="stylesheet" href="https://fonts.googleapis.com/css2?family=Oswald:wght@300;400;500&family=Open+Sans:wght@400;600;700&display=swap">
<style>
:root{
  --ink:#2a2420;
  --header:#231d19;
  --nav:#2f2924;
  --gold:#a5865a;
  --gold-dark:#8a6d45;
  --sand:#efe8da;
  --paper:#ffffff;
  --text:#4a4440;
  --muted:#8a837c;
  --photo-sky:#9fb4c4;
  --photo-house:#8a6a52;
}
*{box-sizing:border-box;margin:0;padding:0}
html,body{width:849px;height:1200px;overflow:hidden}
body{background:var(--paper);font-family:"Open Sans",Arial,sans-serif;color:var(--text);font-size:7.5px;line-height:1.45;position:relative}
/* header */
.site-header{position:absolute;top:0;left:0;width:849px;height:108px;background:var(--header)}
.brand{position:absolute;left:80px;top:30px;display:flex;align-items:center;gap:8px;color:var(--gold);font-family:"Oswald",sans-serif;font-weight:500;font-size:24px;letter-spacing:.5px}
.brand-mark{width:14px;height:14px;background:var(--gold)}
.signup{position:absolute;right:79px;top:30px;display:flex;gap:6px}
.signup-fields{display:flex;flex-direction:column;gap:4px}
.signup-field{width:132px;height:16px;background:#fff;border:1px solid #bbb;font-size:7px;color:var(--muted);padding:2px 5px}
.signup-btn{width:62px;height:36px;background:var(--gold);color:#fff;font-family:"Oswald",sans-serif;font-size:11px;display:flex;align-items:center;justify-content:center;letter-spacing:.5px}
/* nav */
.main-nav{position:absolute;top:108px;left:0;width:849px;height:32px;background:var(--nav)}
.main-nav ul{list-style:none;position:absolute;left:80px;width:690px;display:flex;height:32px}
.main-nav li{flex:1;color:#e8dfd0;font-family:"Oswald",sans-serif;font-size:8.5px;display:flex;align-items:center;justify-content:center;letter-spacing:.3px;position:relative}
.main-nav li.active{background:var(--gold);color:#fff}
.dropdown{position:absolute;top:32px;left:0;width:104px;background:rgba(35,29,25,.92);z-index:3}
.dropdown div{padding:5px 8px;font-family:"Open Sans",sans-serif;font-size:7px;color:#eee;border-bottom:1px solid #4a423b}
.dropdown div:first-child{background:var(--gold)}
/* hero */
.hero{position:absolute;top:140px;left:0;width:849px;height:338px;background:linear-gradient(180deg,var(--photo-sky) 0%,#c9c3b6 35%,var(--photo-house) 60%,#5e6b4c 82%,#9a9690 100%)}
.hero-arrow{position:absolute;top:158px;width:18px;height:18px;border-radius:50%;background:#fff;display:flex;align-items:center;justify-content:center}
.hero-arrow.prev{left:12px}.hero-arrow.next{right:12px}
/* about band */
.about-band{position:absolute;top:478px;left:0;width:849px;height:230px;background:var(--sand)}
.about{position:absolute;left:80px;top:22px;width:375px}
.sec-title{font-family:"Oswald",sans-serif;font-weight:300;font-size:17px;color:var(--ink);letter-spacing:.5px;border-left:3px solid var(--gold);padding-left:7px;line-height:1}
.sec-title span{color:var(--gold)}
.about p{margin-top:12px;font-size:7.2px;color:var(--text)}
.cta{position:absolute;left:478px;top:22px;width:292px}
.cta ul{list-style:none;margin-top:12px}
.cta li{font-size:7.5px;padding:5px 0 5px 9px;border-bottom:1px dotted #c9bda6;position:relative}
.cta li::before{content:"";position:absolute;left:0;top:9px;width:4px;height:4px;background:var(--gold)}
/* content */
.bar{height:22px;background:var(--gold-dark);color:#fff;font-family:"Oswald",sans-serif;font-size:10.5px;padding-left:8px;display:flex;align-items:center;letter-spacing:.5px}
.col-left{position:absolute;left:80px;top:716px;width:480px}
.col-right{position:absolute;left:582px;top:716px;width:188px}
.property{display:flex;gap:14px;padding:10px 0 12px;height:152px}
.property-photo{width:88px;height:100px;flex:none;background:linear-gradient(180deg,#6f8a63,#2e2b2a 55%,#4a5a3e)}
.property h3{font-family:"Oswald",sans-serif;font-weight:500;font-size:8.5px;color:var(--ink);letter-spacing:.3px}
.property p{margin-top:6px;font-size:6.8px}
.actions{display:flex;gap:6px;justify-content:flex-end;margin-top:10px}
.btn{height:12px;padding:0 8px 0 4px;border-radius:6px;background:var(--ink);color:#fff;font-size:6px;display:flex;align-items:center;gap:3px}
.btn i{width:6px;height:6px;border-radius:50%;background:#fff;display:block}
.auction{padding-top:8px}
.auction-photo{height:66px;background:linear-gradient(180deg,#b7c3b5,#7b6a4f)}
.auction-tag{background:var(--ink);color:#e7d9c0;font-size:6px;padding:2px 5px;font-family:"Oswald",sans-serif;letter-spacing:.3px}
.auction .date{font-weight:700;font-size:7px;color:var(--gold-dark);margin-top:6px}
.auction p{font-size:6.6px;margin-top:3px}
.more{display:inline-block;margin-top:6px;background:var(--gold);color:#fff;font-size:6px;padding:2px 7px}
.news-list{padding-top:10px;height:154px}
.news{display:flex;gap:7px;margin-bottom:12px}
.news-thumb{width:46px;height:38px;flex:none;background:linear-gradient(180deg,#a9b7c3,#8c7256)}
.news p{font-size:6.4px}
.news .date{font-size:6px;color:var(--gold-dark);text-align:right;margin-top:3px}
/* footer */
.site-footer{position:absolute;top:1106px;left:0;width:849px;height:94px;background:var(--header);color:#d8cfc2}
.contact{position:absolute;left:80px;top:12px;font-size:7px;line-height:1.55;font-style:normal}
.contact strong{color:#fff}
.badges{position:absolute;right:79px;top:28px;display:flex;gap:12px;align-items:center}
.badge{background:#d8cfc2}
</style>
</head>
<body>
<header class="site-header">
  <div class="brand"><span class="brand-mark"></span>Tolvey Companies</div>
  <form class="signup">
    <div class="signup-fields">
      <div class="signup-field">Enter Name</div>
      <div class="signup-field">Enter Email</div>
    </div>
    <div class="signup-btn">SUBMIT</div>
  </form>
</header>

<nav class="main-nav">
  <ul>
    <li>HOME</li>
    <li>TOLVEY SERVICES</li>
    <li>FEATURED PROJECTS</li>
    <li>RESULTS
      <div class="dropdown"><div>Auction Results</div><div>Sales Results</div></div>
    </li>
    <li>BUYING/SELLING</li>
    <li>ABOUT TOLVEY</li>
    <li class="active">CONTACT US</li>
  </ul>
</nav>

<section class="hero" role="img" aria-label="Slideshow photo of a large two-storey stone and shingle home with garage and driveway">
  <div class="hero-arrow prev"><svg width="8" height="8" viewBox="0 0 8 8"><path d="M5.5 1 2.5 4l3 3" fill="none" stroke="#333" stroke-width="1.4"/></svg></div>
  <div class="hero-arrow next"><svg width="8" height="8" viewBox="0 0 8 8"><path d="M2.5 1l3 3-3 3" fill="none" stroke="#333" stroke-width="1.4"/></svg></div>
</section>

<section class="about-band">
  <div class="about">
    <h2 class="sec-title"><span>ABOUT</span> TOLVEY COMPANIES</h2>
    <p>Lorem ipsum dolor sit amet, consectetur adipiscing elit. Quisque dapibus accumsan orci, pretium eleifend arcu adipiscing eget. Fusce accumsan facilisis tincidunt. Phasellus tempor enim purus, vitae venenatis orci. Ut imperdiet hendrerit pulvinar. Cras id tellus a enim condimentum mollis at et tellus. Mauris dolor magna, vestibulum elementum eu dictum eu.</p>
    <p>Fermentum in nibh. Praesent at dui lectus, vel facilisis sem. Praesent commodo malesuada urna, quis convallis risus dictum et. Nunc dapibus interdum libero.</p>
  </div>
  <div class="cta">
    <h2 class="sec-title"><span>CALL</span> TO ACTION</h2>
    <ul>
      <li>Marketing Consultation</li>
      <li>Marketing Plan Implementation</li>
      <li>Coordination of Related Marketing Services</li>
      <li>Featured Projects</li>
      <li>Negotiated Sales</li>
    </ul>
  </div>
</section>

<main>
  <div class="col-left">
    <div class="bar">FEATURED PROPERTIES</div>
    <article class="property">
      <div class="property-photo" role="img" aria-label="Property photo with furniture and antiques"></div>
      <div>
        <h3>FURNITURE * ANTIQUES * COLLECTIBLES</h3>
        <p>Lorem Ipsum has been the industry's standard dummy text ever since the 1500s, when an unknown printer took a galley of type and scrambled it to make a type specimen book.</p>
        <p>It has survived not only five centuries, but also the leap into electronic typesetting, remaining essentially unchanged since the 1960s.</p>
        <div class="actions"><span class="btn"><i></i>Details</span><span class="btn"><i></i>Gallery</span></div>
      </div>
    </article>
    <div class="bar">FEATURED PROPERTIES</div>
    <article class="property">
      <div class="property-photo" role="img" aria-label="Property photo with furniture and collectibles"></div>
      <div>
        <h3>FURNITURE * ANTIQUES * COLLECTIBLES</h3>
        <p>Lorem Ipsum has been the industry's standard dummy text ever since the 1500s, when an unknown printer took a galley of type and scrambled it to make a type specimen book.</p>
        <p>It has survived not only five centuries, but also the leap into electronic typesetting, remaining essentially unchanged since the 1960s.</p>
        <div class="actions"><span class="btn"><i></i>Details</span><span class="btn"><i></i>Gallery</span></div>
      </div>
    </article>
  </div>

  <aside class="col-right">
    <div class="bar">FEATURED AUCTIONS</div>
    <div class="auction">
      <div class="auction-tag">TRACTOR | 14 LOTS | UNCOMMON</div>
      <div class="auction-photo" role="img" aria-label="Photo of a tractor up for auction"></div>
      <div class="date">Friday, March 15, 2013 at 10:30 AM</div>
      <p>Lorem ipsum dolor sit amet, sale of fine farming and equipment.</p>
      <span class="more">read more</span>
    </div>
    <div class="bar" style="margin-top:22px">NEWS &amp; EVENTS</div>
    <div class="news-list">
      <div class="news">
        <div class="news-thumb" role="img" aria-label="News photo of a home"></div>
        <div><p>Lorem ipsum dolor sit amet, consectetur adipiscing elit, sed do eiusmod tempor incididunt ut labore.</p><div class="date">January 13, 2013</div></div>
      </div>
      <div class="news">
        <div class="news-thumb" role="img" aria-label="News photo of a home"></div>
        <div><p>Lorem ipsum dolor sit amet, consectetur adipiscing elit, sed do eiusmod tempor incididunt ut labore.</p><div class="date">January 13, 2013</div></div>
      </div>
    </div>
  </aside>
</main>

<footer class="site-footer">
  <address class="contact">
    <strong>Tolvey Companies, Inc</strong><br>
    P.O. Box 4382<br>
    Harlow Falls, WI 54897<br>
    tolvey@tolveycompanies.example<br>
    (608) 555-0187 • Fax (608) 555-0143
  </address>
  <div class="badges">
    <div class="badge" style="width:28px;height:28px;border-radius:50%"></div>
    <div class="badge" style="width:22px;height:28px"></div>
    <div class="badge" style="width:40px;height:24px"></div>
    <svg width="30" height="28" viewBox="0 0 30 28"><path d="M15 1 29 27H1z" fill="#d8cfc2"/></svg>
  </div>
</footer>
</body>
</html>
```